Acupuncture Medspa needs a business card design

I need a business card design that looks professional, has a spa-like quality and can offer a promo on the back. Initial promo is "First session free". The tagline of NeedleNook is: Refresh, Restore, Rejuvenate.

NeedleNook is a membership-based acupuncture medspa that offers acupuncture, cupping, and herbal therapies. Members choose between the "Refresh" membership which is for stress relief, or "Restore" which is for treating health conditions, and lastly "Rejuvenate" which is for natural facial enhancement.

Industry/Entity Type

Health And Wellness

Contact Information for Business Card

Coral Haskins, MAC, L.Ac.
612-555-0193
www.needlenook-example.com

Font styles to use
Serif
Sans Serif

Colors

Designer to choose colors to be used in the design.

Requirements
Must have
• The project must have NeedleNook logo, promo on the back, and contact information
Nice to have
• I would like to see the colors of the logo used.

```html
<!DOCTYPE html>
<html lang="en">
<head>
<meta charset="utf-8">
<title>NeedleNook Business Card</title>
<link href="https://fonts.googleapis.com/css2?family=Montserrat:wght@500;600&family=Open+Sans:wght@400&display=swap" rel="stylesheet">
<style>
  :root {
    --teal: #0f8080;
    --teal-light: #4fc7bd;
    --teal-faint: #e3f1f0;
    --ink: #3a2620;
    --paper: #ffffff;
    --backdrop: #eceeee;
    --shadow: rgba(0,0,0,0.12);
  }
  * { margin: 0; padding: 0; box-sizing: border-box; }
  html, body { width: 1200px; height: 900px; overflow: hidden; }
  body {
    background: var(--backdrop);
    display: flex;
    flex-direction: column;
    align-items: center;
    justify-content: center;
    gap: 40px;
    font-family: "Open Sans", sans-serif;
  }
  .card {
    position: relative;
    width: 700px;
    height: 400px;
    background: var(--paper);
    box-shadow: 0 6px 18px var(--shadow);
    overflow: hidden;
  }
  .ring {
    position: absolute;
    border-radius: 50%;
    border: 12px solid var(--teal);
  }
  .outer-arc {
    position: absolute;
    border-radius: 50%;
    border: 3px solid transparent;
    border-left-color: var(--teal);
  }
  .front .ring { width: 360px; height: 360px; left: 40px; top: 20px; }
  .front .outer-arc { width: 390px; height: 390px; left: 18px; top: 5px; transform: rotate(20deg); }
  .brand-name {
    position: absolute;
    font-family: "Montserrat", sans-serif;
    font-weight: 600;
    color: var(--teal);
    letter-spacing: 3px;
    text-transform: uppercase;
    text-align: center;
  }
  .front .brand-name { left: 40px; width: 360px; top: 178px; font-size: 36px; }
  .contact {
    position: absolute;
    left: 440px;
    top: 90px;
    width: 240px;
    display: flex;
    flex-direction: column;
    align-items: center;
    gap: 14px;
    color: var(--ink);
    font-size: 17px;
    text-align: center;
  }
  .icon { width: 40px; height: 40px; }
  .back .ring { width: 300px; height: 300px; left: 60px; top: 50px; }
  .back .outer-arc { width: 326px; height: 326px; left: 47px; top: 37px; transform: rotate(20deg); }
  .back .brand-name { left: 60px; width: 300px; top: 182px; font-size: 28px; }
  .promo {
    position: absolute;
    left: 390px;
    top: 110px;
    width: 290px;
    text-align: center;
  }
  .promo-offer {
    font-family: "Montserrat", sans-serif;
    font-weight: 600;
    font-size: 26px;
    color: var(--teal);
    line-height: 1.25;
  }
  .promo-tagline {
    margin-top: 14px;
    font-size: 15px;
    color: var(--ink);
  }
  .web-band {
    position: absolute;
    right: 0;
    bottom: 40px;
    width: 360px;
    height: 50px;
    display: flex;
    align-items: center;
    gap: 12px;
    padding-left: 28px;
    background: linear-gradient(90deg, rgba(79,199,189,0) 0%, var(--teal-light) 35%, var(--teal-light) 75%, rgba(79,199,189,0) 100%);
    color: var(--ink);
    font-size: 15px;
  }
  .web-band .icon { width: 30px; height: 30px; }
</style>
</head>
<body>
  <section class="card front">
    <div class="outer-arc"></div>
    <div class="ring"></div>
    <div class="brand-name">NeedleNook</div>
    <div class="contact">
      <svg class="icon" viewBox="0 0 40 40" aria-hidden="true">
        <ellipse cx="20" cy="35" rx="14" ry="4" fill="#e6e0de"/>
        <path d="M20 36 C12 26 8 21 8 15 a12 12 0 0 1 24 0 c0 6 -4 11 -12 21z" fill="var(--teal)"/>
        <circle cx="20" cy="15" r="7" fill="#fff"/>
        <path d="M16.5 15 l2.5 2.5 l4.5 -5" stroke="var(--teal)" stroke-width="2" fill="none"/>
      </svg>
      <div class="person">Coral Haskins, MAC, L.Ac.</div>
      <svg class="icon" viewBox="0 0 40 40" aria-hidden="true">
        <rect x="11" y="10" width="18" height="28" rx="3" fill="var(--teal)"/>
        <rect x="14" y="14" width="12" height="8" fill="#fff"/>
        <g fill="#fff"><rect x="14" y="26" width="3" height="3"/><rect x="18.5" y="26" width="3" height="3"/><rect x="23" y="26" width="3" height="3"/><rect x="14" y="31" width="3" height="3"/><rect x="18.5" y="31" width="3" height="3"/><rect x="23" y="31" width="3" height="3"/></g>
        <path d="M16 6 a8 8 0 0 1 8 0 M13 3 a12 12 0 0 1 14 0" stroke="var(--teal)" stroke-width="1.8" fill="none"/>
      </svg>
      <div class="phone">612-555-0193</div>
    </div>
  </section>

  <section class="card back">
    <div class="outer-arc"></div>
    <div class="ring"></div>
    <div class="brand-name">NeedleNook</div>
    <div class="promo">
      <p class="promo-offer">First session free</p>
      <p class="promo-tagline">Refresh, Restore, Rejuvenate</p>
    </div>
    <div class="web-band">
      <svg class="icon" viewBox="0 0 30 30" aria-hidden="true">
        <g stroke="var(--ink)" stroke-width="1.6" fill="none">
          <circle cx="15" cy="15" r="12"/>
          <ellipse cx="15" cy="15" rx="5" ry="12"/>
          <path d="M3 15 h24 M5 9 h20 M5 21 h20"/>
        </g>
      </svg>
      <span class="web">www.needlenook-example.com</span>
    </div>
  </section>
</body>
</html>
```